Professional business card for the wholesale of metals, chemicals and waste

We are an established company in the wholesale trade of metals, chemicals and waste and are looking for a creative, professional design for our business card. The business card should reflect the values of our company - competence, reliability and innovative strength. It should convey both industry expertise and a modern, trustworthy image.
Important information for the design:

Logo: Our company logo must be prominently placed on the business card.
Colors: Please refer to the colors used on our website www.okr-gmbh.at. These colors should appear in the design to maintain the visual identity of our company.

QR Code: The business card should contain a QR code that contains all the information listed on the business card.
Font: Choose clear, easy-to-read fonts that reflect a modern, professional look.
Layout: The design should be clear and structured so that both text and visual elements (logo, QR code) are in a balanced relationship to each other.

Information that should appear on the business card:

Company name: OKR Handelsagenturen GmbH
Title: Dipl.-Ing.
Name: Lukas Fenwald
Position: Managing Director of Operations & Corporate Development
Phone: +43 4186 5921 48
Mobile: +43 664 58 37 216
Email: lukas.fenwald@okr-gmbh.at
Homepage: www.okr-gmbh.at

Design style:

Industry: Industrial yet modern style that conveys competence and trust.
Message: The business card should present our company as a leading supplier in the wholesale trade of metals, chemicals and waste – reliable, professional and innovative.
Target group: Our target group consists of B2B customers and industry contacts who are looking for high-quality products and services in the areas of metal trading, chemicals and waste management.

We look forward to creative designs that reflect our professional identity and are also modern and appealing. Your design should make a statement for our company!

```html
<!DOCTYPE html>
<html lang="en">
<head>
<meta charset="utf-8">
<title>OKR Handelsagenturen GmbH – Business Card</title>
<link href="https://fonts.googleapis.com/css2?family=Roboto:ital,wght@0,300;0,400;0,700;1,300;1,400&display=swap" rel="stylesheet">
<style>
  :root {
    --stage: #a9a8a9;
    --violet: #4f47a8;
    --violet-deep: #3d3690;
    --steel-blue: #2f9be0;
    --glow: #6fd2ff;
    --band-dark: #1b1d2e;
    --silver-light: #f4f5f7;
    --silver-mid: #c9ccd1;
    --silver-dark: #a4a8ae;
    --navy: #1e2452;
    --white: #ffffff;
  }
  html, body {
    margin: 0;
    padding: 0;
    width: 1200px;
    height: 1200px;
    overflow: hidden;
    background: var(--stage);
    font-family: "Roboto", Arial, sans-serif;
  }
  .card {
    position: absolute;
    left: 160px;
    width: 880px;
    height: 515px;
    overflow: hidden;
    box-shadow: 0 4px 10px rgba(0,0,0,0.35);
  }
  /* Front */
  .card-front {
    top: 62px;
    background:
      linear-gradient(90deg,
        var(--violet-deep) 0%, var(--violet) 30%,
        #3f6fd0 42%, var(--steel-blue) 48%, #5a5fc0 56%,
        var(--steel-blue) 63%, var(--glow) 66%, #4b55b8 72%,
        var(--violet) 85%, var(--violet-deep) 100%);
  }
  .brushed-sheen {
    position: absolute;
    inset: 0;
    background: repeating-linear-gradient(0deg,
      rgba(255,255,255,0.05) 0px, rgba(255,255,255,0.05) 1px,
      rgba(0,0,0,0.04) 2px, rgba(0,0,0,0) 4px);
  }
  .top-bands { position: absolute; left: 0; top: 0; }
  .person-name {
    position: absolute;
    left: 59px;
    top: 150px;
    margin: 0;
    font-size: 36px;
    font-weight: 700;
    line-height: 44px;
    color: var(--white);
    white-space: nowrap;
  }
  .person-role {
    position: absolute;
    left: 59px;
    top: 214px;
    margin: 0;
    font-size: 20.5px;
    font-style: italic;
    font-weight: 300;
    line-height: 29px;
    color: var(--white);
    white-space: nowrap;
  }
  .contact-list {
    position: absolute;
    left: 59px;
    top: 310px;
    margin: 0;
    padding: 0;
    list-style: none;
    color: var(--white);
    font-size: 24px;
    font-weight: 300;
  }
  .contact-list li {
    display: flex;
    align-items: center;
    height: 40.5px;
    white-space: nowrap;
  }
  .contact-icon {
    width: 18px;
    height: 18px;
    margin-right: 17px;
    fill: var(--white);
    flex: none;
  }
  .brand-front {
    position: absolute;
    left: 520px;
    top: 246px;
    width: 300px;
    text-align: center;
    color: var(--white);
  }
  .brand-name {
    display: block;
    font-size: 84px;
    font-weight: 700;
    letter-spacing: 2px;
    line-height: 1;
  }
  .brand-title {
    display: block;
    margin-top: 70px;
    font-size: 33px;
    font-weight: 700;
    line-height: 1.2;
  }
  /* Back */
  .card-back {
    top: 625px;
    background:
      linear-gradient(90deg,
        var(--silver-dark) 0%, var(--silver-light) 20%, var(--silver-mid) 38%,
        var(--silver-light) 55%, var(--silver-mid) 72%, var(--silver-light) 88%,
        var(--silver-dark) 100%);
  }
  .perforated-band {
    position: absolute;
    left: 0;
    width: 880px;
    background: var(--band-dark);
  }
  .perforated-band.top { top: 22px; height: 14px; }
  .perforated-band.bottom { bottom: 8px; height: 14px; }
  .band-rim {
    position: absolute;
    left: 0;
    width: 880px;
    height: 3px;
    background: #5a5d66;
  }
  .rim-top-outer { top: 19px; }
  .rim-top-inner { top: 36px; }
  .rim-bottom-inner { bottom: 22px; }
  .brand-back {
    position: absolute;
    left: 0;
    top: 195px;
    width: 880px;
    text-align: center;
    color: var(--navy);
  }
  .brand-back .brand-title { margin-top: 68px; font-size: 35px; }
</style>
</head>
<body>

<section class="card card-front" aria-label="Business card front">
  <div class="brushed-sheen"></div>
  <svg class="top-bands" width="880" height="125" viewBox="0 0 880 125">
    <defs>
      <linearGradient id="stripe-glow" x1="0" x2="1" y1="0" y2="0">
        <stop offset="0" stop-color="#3a3f9a"/>
        <stop offset="0.45" stop-color="#3aa8ff"/>
        <stop offset="0.6" stop-color="#8fe0ff"/>
        <stop offset="1" stop-color="#3a3f9a"/>
      </linearGradient>
    </defs>
    <rect x="0" y="0" width="880" height="125" fill="#22243a"/>
    <rect x="0" y="34" width="880" height="12" fill="url(#stripe-glow)"/>
    <rect x="0" y="56" width="880" height="6" fill="url(#stripe-glow)"/>
    <rect x="0" y="72" width="880" height="14" fill="url(#stripe-glow)"/>
    <rect x="0" y="96" width="880" height="18" fill="url(#stripe-glow)" opacity="0.85"/>
    <rect x="0" y="116" width="880" height="9" fill="#1b1d2e"/>
  </svg>

  <h1 class="person-name">Lukas Fenwald</h1>
  <p class="person-role">Managing Director of Operations<br>&amp; Corporate Development</p>

  <ul class="contact-list">
    <li>
      <svg class="contact-icon" viewBox="0 0 24 24"><path d="M6.6 10.8a15.1 15.1 0 0 0 6.6 6.6l2.2-2.2c.3-.3.7-.4 1-.2 1.1.4 2.3.6 3.6.6.6 0 1 .4 1 1V20c0 .6-.4 1-1 1A17 17 0 0 1 3 4c0-.6.4-1 1-1h3.5c.6 0 1 .4 1 1 0 1.3.2 2.5.6 3.6.1.3 0 .7-.2 1z"/></svg>
      +43 4186 5921 48
    </li>
    <li>
      <svg class="contact-icon" viewBox="0 0 24 24"><path d="M7 1h10a2 2 0 0 1 2 2v18a2 2 0 0 1-2 2H7a2 2 0 0 1-2-2V3a2 2 0 0 1 2-2zm0 3v15h10V4zm4 16v1.5h2V20z"/></svg>
      +43 664 58 37 216
    </li>
    <li>
      <svg class="contact-icon" viewBox="0 0 24 24"><path d="M2 5h20v14H2zm2 2v.5l8 5 8-5V7l-8 5z"/></svg>
      lukas.fenwald@okr-gmbh.at
    </li>
    <li>
      <svg class="contact-icon" viewBox="0 0 24 24"><path d="M12 2a10 10 0 1 0 0 20 10 10 0 0 0 0-20zm6.9 6h-3a15 15 0 0 0-1.3-3.9A8 8 0 0 1 18.9 8zM12 4c.8 1.2 1.5 2.5 1.9 4h-3.8c.4-1.5 1.1-2.8 1.9-4zM4.3 14a8 8 0 0 1 0-4h3.4a16 16 0 0 0 0 4zm.8 2h3a15 15 0 0 0 1.3 3.9A8 8 0 0 1 5.1 16zm3-8h-3a8 8 0 0 1 4.3-3.9C8.7 5.3 8.3 6.6 8 8zM12 20c-.8-1.2-1.5-2.5-1.9-4h3.8c-.4 1.5-1.1 2.8-1.9 4zm2.3-6H9.7a14 14 0 0 1 0-4h4.6a14 14 0 0 1 0 4zm.3 5.9c.6-1.2 1-2.5 1.3-3.9h3a8 8 0 0 1-4.3 3.9zm1.7-5.9a16 16 0 0 0 0-4h3.4a8 8 0 0 1 0 4z"/></svg>
      www.okr-gmbh.at
    </li>
  </ul>

  <div class="brand-front">
    <span class="brand-name">OKR</span>
    <span class="brand-title">Dipl.-Ing.</span>
  </div>
</section>

<section class="card card-back" aria-label="Business card back">
  <div class="brushed-sheen"></div>
  <div class="band-rim rim-top-outer"></div>
  <div class="perforated-band top" role="img" aria-label="Perforated metal strip"></div>
  <div class="band-rim rim-top-inner"></div>
  <div class="band-rim rim-bottom-inner"></div>
  <div class="perforated-band bottom" role="img" aria-label="Perforated metal strip"></div>
  <div class="brand-back">
    <span class="brand-name">OKR</span>
    <span class="brand-title">Dipl.-Ing.</span>
  </div>
</section>

</body>
</html>
```